Well Designed, Impactful Business Card

I need a new business card designed that incorporates our company colors, looks very well designed, and is of the highest quality as that reflects the work we do as a professional services firm.

We would like it to incorporate a QR code and will link to an article we have written as a hook for potential clients. Designs should use the colors uploaded and can incorporate other colors to supplement the ones attached. The design should communicate professionalism, design, quality, and competence. Tagline can be used, but not required. Alternatively, a new one created. Current tagline is "Faster Insight, More Engagement"

I would like for the two sides to be contrasting. If the front is colored, the back should be white (or light vs dark colors).

Old company website is here www.brambleforge.net

```html
<!DOCTYPE html>
<html lang="en">
<head>
<meta charset="utf-8">
<title>Bramble Forge Business Card</title>
<link href="https://fonts.googleapis.com/css2?family=Montserrat:wght@400;500;700&display=swap" rel="stylesheet">
<style>
  :root {
    --backdrop: #adaeaa;
    --card-white: #ffffff;
    --charcoal: #554e4a;
    --orange: #f39323;
    --stone: #8a807a;
    --text-light: #ffffff;
  }
  * { margin: 0; padding: 0; box-sizing: border-box; }
  html, body {
    width: 1200px; height: 801px; overflow: hidden;
    background: var(--backdrop);
    font-family: "Montserrat", sans-serif;
  }
  .canvas {
    position: relative; width: 1200px; height: 801px;
  }
  .card {
    position: absolute; top: 246px;
    width: 540px; height: 308px;
    background: var(--card-white);
    border-bottom: 4px solid var(--orange);
    box-shadow: 0 12px 30px rgba(0,0,0,0.25);
    overflow: hidden;
  }
  .card--front { left: 40px; }
  .card--back { left: 620px; }
  .front-bands { position: absolute; inset: 0; width: 100%; height: 100%; }
  .wordmark {
    position: absolute;
    display: flex; align-items: center; gap: 10px;
    font-weight: 500; color: var(--charcoal);
    letter-spacing: 0.12em; text-transform: uppercase;
  }
  .wordmark__square {
    display: block; width: 14px; height: 14px; background: var(--orange);
  }
  .card--front .wordmark { top: 52px; left: 160px; font-size: 22px; }
  .card--back .wordmark {
    top: 50%; left: 50%; transform: translate(-50%, -50%);
    font-size: 30px; gap: 14px;
  }
  .card--back .wordmark__square { width: 18px; height: 18px; }
  .holder {
    position: absolute; right: 26px; top: 158px; text-align: right;
  }
  .holder__name {
    color: var(--orange); font-weight: 700; font-size: 19px; letter-spacing: 0.06em;
  }
  .holder__title {
    color: var(--text-light); font-size: 11px; letter-spacing: 0.1em; margin-top: 3px;
  }
  .holder__marker {
    position: absolute; right: 0; top: 96px;
  }
  .contacts {
    position: absolute; left: 26px; bottom: 22px;
    list-style: none; color: var(--text-light); font-size: 12px; line-height: 1.55;
  }
  .contacts li { display: flex; align-items: center; gap: 8px; }
  .contacts svg { width: 10px; height: 10px; flex: none; }
</style>
</head>
<body>
<main class="canvas">
  <section class="card card--front" aria-label="Card front">
    <svg class="front-bands" viewBox="0 0 540 308" preserveAspectRatio="none" aria-hidden="true">
      <path d="M0,222 Q300,176 540,34 L540,308 L0,308 Z" fill="var(--stone)"/>
      <path d="M0,224 Q300,180 540,38 L540,308 L0,308 Z" fill="var(--orange)"/>
      <path d="M0,228 Q300,190 540,56 L540,308 L0,308 Z" fill="var(--card-white)"/>
      <path d="M0,232 Q300,196 540,66 L540,308 L0,308 Z" fill="var(--charcoal)"/>
    </svg>
    <div class="wordmark"><span class="wordmark__square"></span>Bramble Forge</div>
    <svg class="holder__marker" width="22" height="14" viewBox="0 0 22 14" aria-hidden="true">
      <path d="M0,0 L22,0 L22,14 Z" fill="var(--orange)"/>
    </svg>
    <div class="holder">
      <p class="holder__name">DANIEL CARVER</p>
      <p class="holder__title">PRESIDENT</p>
    </div>
    <ul class="contacts">
      <li><svg viewBox="0 0 10 10" aria-hidden="true"><path d="M2,1 L4,1 L4.5,3 L3.3,3.8 Q4.5,6 6.2,6.7 L7,5.5 L9,6 L9,8 Q5,9 2,5 Q1,3 2,1Z" fill="var(--orange)"/></svg>555-210-4478</li>
      <li><svg viewBox="0 0 10 10" aria-hidden="true"><rect x="0.7" y="2" width="8.6" height="6" fill="none" stroke="var(--orange)" stroke-width="1.2"/><path d="M1,2.5 L5,5.5 L9,2.5" fill="none" stroke="var(--orange)" stroke-width="1.2"/></svg>daniel@brambleforge.net</li>
      <li><svg viewBox="0 0 10 10" aria-hidden="true"><circle cx="5" cy="5" r="4.2" fill="none" stroke="var(--orange)" stroke-width="1.2"/><path d="M1,5 H9 M5,1 Q2.5,5 5,9 Q7.5,5 5,1" fill="none" stroke="var(--orange)" stroke-width="1"/></svg>www.brambleforge.net</li>
    </ul>
  </section>

  <section class="card card--back" aria-label="Card back">
    <div class="wordmark"><span class="wordmark__square"></span>Bramble Forge</div>
  </section>
</main>
</body>
</html>
```